Verenka Dance Conservatory (Moscow) needs a Book Cover Design

It is an academic book of ballet lessons from one of the greatests BALLET masters of XX century. Grigori Lemekhin published his book (ballet bible) in 70's and our new book is the next part of it.
G. Lemekhin performed in Verenka Dance from 1920 to 1935 in classical roles. He taught at Stolnaya Movement Institute (Verenka Dance Conservatory) from 1923 to 1960. He was general director and artistic director from 1942-1945 and again in 1953.
Lemekhin was co-autor of the "Principles of formal stage practice" 1940 and autor of "Stage craft for the leading performer".
Our book containes his 95 lessons from 1960 to 1963.

In attachment you can find more info about the format of the book, langage and images.

Target Market(s)

Ballet professiaonals, enthusiasts, ballet lovers

Industry/Entity Type

School

Font styles to use
Serif

Requirements
Must have
• The images from previous Lemekhin's book

```html
<!DOCTYPE html>
<html lang="en">
<head>
<meta charset="utf-8">
<title>Ballet Lessons – Book Cover</title>
<link rel="stylesheet" href="https://fonts.googleapis.com/css2?family=Cinzel:wght@400;500&family=Cormorant+Garamond:wght@500&display=swap">
<style>
  :root {
    --page-bg: #f4f4f2;
    --teal: #557f79;
    --teal-deep: #4a736d;
    --feet-ink: #37605a;
    --cream: #e7e4dd;
    --mist: #b4c2be;
    --sage: #8fa6a1;
    --dancer-light: #b7c0bb;
    --dancer-mid: #8fa39f;
    --dancer-dark: #4f7a74;
    --title-ink: #ece8df;
    --subtitle-ink: #5b8a84;
    --name-ink: #4a7a73;
    --author-ink: #ffffff;
  }
  * { box-sizing: border-box; margin: 0; padding: 0; }
  html, body {
    width: 1200px;
    height: 1000px;
    overflow: hidden;
    background: var(--page-bg);
  }
  .canvas {
    position: relative;
    width: 1200px;
    height: 1000px;
  }
  .cover {
    position: absolute;
    left: 275px;
    top: 50px;
    width: 650px;
    height: 900px;
    overflow: hidden;
    background: linear-gradient(to bottom,
      var(--cream) 0%, var(--cream) 68%, var(--mist) 86%, var(--sage) 100%);
    box-shadow: 0 10px 30px rgba(0,0,0,0.18);
  }
  .cover__band {
    position: absolute;
    inset: 0 0 auto 0;
    height: 345px;
    background: linear-gradient(to bottom, var(--teal-deep) 0%, var(--teal) 100%);
  }
  .feet-positions {
    position: absolute;
    left: 110px;
    top: 0;
    width: 430px;
    height: 125px;
    background: var(--feet-ink);
    border-radius: 0 0 6px 6px;
  }
  .title {
    position: absolute;
    left: 0;
    right: 0;
    top: 152px;
    text-align: center;
    font-family: "Cinzel", serif;
    font-weight: 400;
    font-size: 78px;
    line-height: 80px;
    letter-spacing: 3px;
    color: var(--title-ink);
  }
  .subtitle {
    position: absolute;
    left: 0;
    right: 0;
    top: 374px;
    text-align: center;
    font-family: "Cinzel", serif;
    color: var(--subtitle-ink);
  }
  .subtitle__lead {
    display: block;
    font-size: 26px;
    line-height: 31px;
    letter-spacing: 1.5px;
  }
  .subtitle__name {
    display: block;
    margin-top: 2px;
    font-size: 42px;
    line-height: 48px;
    letter-spacing: 1.5px;
    font-weight: 500;
    color: var(--name-ink);
  }
  .dancers {
    position: absolute;
    left: 140px;
    top: 505px;
    width: 380px;
    height: 270px;
    border-radius: 6px;
    background: linear-gradient(to right,
      var(--dancer-light) 0%, var(--dancer-mid) 45%, var(--dancer-dark) 100%);
  }
  .author {
    position: absolute;
    left: 0;
    right: 0;
    top: 812px;
    text-align: center;
    font-family: "Cormorant Garamond", serif;
    font-weight: 500;
    font-size: 30px;
    color: var(--author-ink);
  }
</style>
</head>
<body>
  <main class="canvas">
    <article class="cover">
      <div class="cover__band"></div>
      <div class="feet-positions" role="img" aria-label="Drawing of legs and feet in the first three ballet positions"></div>
      <h1 class="title">Ballet<br>Lessons</h1>
      <p class="subtitle">
        <span class="subtitle__lead">The 95 Ballet Lessons of</span>
        <span class="subtitle__lead">The Great Russian Master</span>
        <span class="subtitle__name">Grigori Lemekhin</span>
      </p>
      <div class="dancers" role="img" aria-label="Sketch of four male dancers in sequence performing a ballet step"></div>
      <p class="author">by Pavel Orlinsky</p>
    </article>
  </main>
</body>
</html>
```